Building and Maintenance Company requires a flyer design, Specialising in domestic and commercial bu

We need a flyer design for a company based in Melbourne Victoria, we want to send the flyer out to businesses to obtain more work.

KEV Building and Construction provides the solution for all your building and maintenance needs

We have a professional and highly regarded team of reliable and skilled tradesmen who specialise in building services, domestic and commercial maintenance and gardening in Victoria and Tasmania.

Include our contact details;
0412 738 206
info@kevbuilding.example.au
www.kevbuilding.example.au

Target Market(s)

Domestic and Commercial Clients looking for building maintenance, window cleaning or gardening

Industry/Entity Type

It Company

Font styles to use
Sans Serif

Colors
33b8a4
474747
ffffff

Requirements
Must have
• Images and colour
Nice to have
• We would like the flyer to have our contact details on it.
• Colourful
• Clearly explains what we do, which is, 'KEV Building and Construction provides the solution for all your building, maintenance and gardening needs.'

```html
<!DOCTYPE html>
<html lang="en">
<head>
<meta charset="utf-8">
<title>KEV Building and Construction – Flyer</title>
<link rel="stylesheet" href="https://fonts.googleapis.com/css2?family=Open+Sans:wght@400;600;700&family=Rajdhani:wght@500&display=swap">
<style>
  :root {
    --teal: #33b8a4;
    --teal-deep: #1f8f86;
    --charcoal: #474747;
    --ink: #2f2f2f;
    --white: #ffffff;
    --stage: #eceeee;
    --paper-haze: #f3f5f5;
  }
  * { box-sizing: border-box; margin: 0; padding: 0; }
  html, body {
    width: 1048px;
    height: 1200px;
    overflow: hidden;
    background: var(--stage);
    font-family: "Open Sans", Arial, sans-serif;
  }
  .flyer {
    position: absolute;
    left: 104px;
    top: 10px;
    width: 840px;
    height: 1180px;
    background: var(--white);
    overflow: hidden;
    box-shadow: 0 4px 18px rgba(0,0,0,0.18);
  }
  .backdrop-top {
    position: absolute;
    left: 0; top: 34px;
    width: 840px; height: 600px;
    background: linear-gradient(135deg, #f7f8f8 0%, #eef0f0 55%, #f4f0dc 100%);
  }
  .backdrop-bottom {
    position: absolute;
    left: 0; top: 940px;
    width: 840px; height: 240px;
    background: linear-gradient(180deg, #f4f5f3 0%, #e6ebe2 60%, #dfe4da 100%);
  }
  .top-bar {
    position: absolute;
    left: 0; top: 34px;
    width: 386px; height: 24px;
    background: var(--ink);
  }
  .worker-photo {
    position: absolute;
    left: 0; top: 58px;
    width: 305px; height: 720px;
    background: linear-gradient(160deg, #4c6a96 0%, #f2c31c 35%, #d9a21a 55%, #3e4440 80%, #c9cdc7 100%);
  }
  .brand {
    position: absolute;
    left: 430px; top: 58px;
    width: 290px;
    text-align: center;
    font-family: "Rajdhani", "Open Sans", sans-serif;
    font-weight: 500;
    color: var(--teal-deep);
    letter-spacing: 3px;
    line-height: 1;
  }
  .brand-name { display: block; font-size: 118px; letter-spacing: 6px; }
  .brand-line { display: block; font-size: 33px; margin-top: 6px; }
  .headline {
    position: absolute;
    left: 330px; top: 318px;
    width: 450px;
    text-align: center;
    line-height: 1;
  }
  .headline-lead { display: block; font-size: 42px; font-weight: 600; color: var(--charcoal); }
  .headline-main { display: block; font-size: 92px; font-weight: 600; color: var(--teal-deep); margin-top: 8px; }
  .headline-amp { display: block; font-size: 30px; font-weight: 700; color: var(--teal-deep); margin-top: -14px; height: 18px; }
  .headline-second { display: block; font-size: 60px; font-weight: 600; color: var(--teal-deep); margin-top: 2px; }
  .headline-end { display: block; font-size: 72px; font-weight: 600; color: var(--charcoal); margin-top: 4px; }
  .rule {
    position: absolute;
    left: 298px; top: 630px;
    width: 542px; height: 4px;
    background: var(--teal);
  }
  .teal-block {
    position: absolute;
    left: 0; top: 773px;
    width: 198px; height: 168px;
    background: linear-gradient(135deg, #7fd3c7 0%, var(--teal) 60%, #2aa592 100%);
  }
  .side-block {
    position: absolute;
    left: 790px; top: 719px;
    width: 50px; height: 114px;
    background: var(--ink);
  }
  .service {
    position: absolute;
    top: 645px;
    width: 280px; height: 296px;
  }
  .service-commercial { left: 204px; }
  .service-domestic { left: 495px; }
  .service-photo { width: 100%; height: 100%; }
  .service-commercial .service-photo {
    background: linear-gradient(160deg, #1c3f7a 0%, #5b8fc9 45%, #9fc0e2 70%, #2a4f88 100%);
  }
  .service-domestic .service-photo {
    background: linear-gradient(170deg, #6a7c96 0%, #8a9a6e 40%, #5f8f3a 70%, #3f6e25 100%);
  }
  .service-label {
    position: absolute;
    left: 0; bottom: 0;
    width: 100%; height: 54px;
    background: rgba(58,58,58,0.85);
    color: var(--white);
    font-size: 24px;
    font-weight: 700;
    text-align: center;
    line-height: 54px;
  }
  .qualities {
    position: absolute;
    left: 0; top: 952px;
    width: 776px; height: 64px;
    background: var(--ink);
    display: flex;
    align-items: center;
    justify-content: space-evenly;
    padding: 0 10px;
    list-style: none;
  }
  .quality {
    display: flex;
    align-items: center;
    gap: 4px;
    color: var(--white);
    font-size: 22px;
    font-weight: 600;
  }
  .quality svg { width: 38px; height: 38px; margin-top: -10px; }
  .contact {
    position: absolute;
    left: 0; top: 1044px;
    width: 776px;
    text-align: center;
  }
  .contact-line {
    font-size: 26px;
    font-weight: 700;
    color: var(--teal-deep);
    letter-spacing: 0.5px;
  }
  .contact-web {
    font-size: 44px;
    font-weight: 700;
    color: var(--charcoal);
    margin-top: 6px;
    letter-spacing: 0.5px;
  }
</style>
</head>
<body>
  <main class="flyer">
    <div class="backdrop-top" role="img" aria-label="Faded architectural plans and builder's tools in the background"></div>
    <div class="backdrop-bottom" role="img" aria-label="Faded photo of a freshly laid lawn"></div>
    <div class="top-bar"></div>
    <div class="worker-photo" role="img" aria-label="Tradesman in a checked shirt carrying a yellow hard hat and toolbox"></div>

    <header class="brand" aria-label="KEV Building and Construction">
      <span class="brand-name">KEV</span>
      <span class="brand-line">BUILDING AND</span>
      <span class="brand-line">CONSTRUCTION</span>
    </header>

    <h1 class="headline">
      <span class="headline-lead">YOUR ULTIMATE</span>
      <span class="headline-main">BUILDING</span>
      <span class="headline-amp">&amp;</span>
      <span class="headline-second">MAINTENANCE</span>
      <span class="headline-end">SOLUTION</span>
    </h1>

    <div class="rule"></div>
    <div class="teal-block"></div>
    <div class="side-block"></div>

    <section class="service service-commercial">
      <div class="service-photo" role="img" aria-label="Window cleaner abseiling down a glass office building"></div>
      <div class="service-label">COMMERCIAL</div>
    </section>
    <section class="service service-domestic">
      <div class="service-photo" role="img" aria-label="Gardener trimming a hedge with a hedge trimmer"></div>
      <div class="service-label">DOMESTIC</div>
    </section>

    <ul class="qualities">
      <li class="quality"><svg viewBox="0 0 40 40" aria-hidden="true"><path d="M4 22 L14 32 L36 4" fill="none" stroke="#33b8a4" stroke-width="4" stroke-linecap="round" stroke-linejoin="round"/></svg>Professional</li>
      <li class="quality"><svg viewBox="0 0 40 40" aria-hidden="true"><path d="M4 22 L14 32 L36 4" fill="none" stroke="#33b8a4" stroke-width="4" stroke-linecap="round" stroke-linejoin="round"/></svg>Highly Regarded</li>
      <li class="quality"><svg viewBox="0 0 40 40" aria-hidden="true"><path d="M4 22 L14 32 L36 4" fill="none" stroke="#33b8a4" stroke-width="4" stroke-linecap="round" stroke-linejoin="round"/></svg>Reliable</li>
      <li class="quality"><svg viewBox="0 0 40 40" aria-hidden="true"><path d="M4 22 L14 32 L36 4" fill="none" stroke="#33b8a4" stroke-width="4" stroke-linecap="round" stroke-linejoin="round"/></svg>Skilled</li>
    </ul>

    <footer class="contact">
      <p class="contact-line">0412 738 206 | INFO@KEVBUILDING.EXAMPLE.AU</p>
      <p class="contact-web">WWW.KEVBUILDING.EXAMPLE.AU</p>
    </footer>
  </main>
</body>
</html>
```